Web design for "Vetted Hammer Hub"

We need a web design for a service that we are providing to consumers. We have 4 products or packages that they can choose from. These vary in terms of inclusions and cost. The basic service that we off is that we interview, reference check and verify insurances on tradespeople before a consumer commits with a tradesperson to complete a job.
The web design will need to incorporate two databases. One database for the consumer buying the services and another database for the tradespeople that are being checked.
The cost will be charged to the consumer. The service will be free for tradespeople to join.
The services will be packages based on what the consumer is requiring. There are 4 packages at varying prices. We will need also need a page that has the payment portal.
We will need a rating system (stars or similar), the ability to upload documents, and to send communications.
Updates

Reason: I have only had one designer submit their designs. Would really appreciate a comparison

Target Market(s)

Professionals, time poor people, mainly female target audience

Industry/Entity Type

Business Service

Number of Pages Required

5+ page

Font styles to use
Sans Serif

Colors
abd036
fece3e
b7a5cd
f68d4d
3176b5
cadf82

Requirements
Must have
• 2 x databases, Payment Portal, star rating

```html
<!DOCTYPE html>
<html lang="en">
<head>
<meta charset="utf-8">
<title>Vetted Hammer Hub</title>
<link href="https://fonts.googleapis.com/css2?family=Open+Sans:ital,wght@0,300;0,400;0,600;0,700;1,400&family=Oswald:wght@300&display=swap" rel="stylesheet">
<style>
:root{
  --orange:#f7931e;
  --orange-soft:#f68d4d;
  --blue:#1f8fd0;
  --teal:#2bb8d3;
  --red:#e05a5a;
  --yellow:#e2c24a;
  --green:#7cc04a;
  --dark:#2a2a2a;
  --ink:#333;
  --muted:#8a8a8a;
  --line:#e4e4e4;
  --beige:#f1ebe1;
  --pale:#f7f7f7;
  --star:#f5a623;
}
*{box-sizing:border-box;margin:0;padding:0}
html,body{width:1200px;height:3261px;overflow:hidden}
body{font-family:"Open Sans",Arial,sans-serif;color:var(--ink);background:#fff;position:relative}
section,header,footer{position:absolute;left:0;width:1200px}
.lorem{font-size:12px;line-height:20px;color:var(--muted)}
.center{text-align:center}
.section-title{font-size:27px;font-weight:300;letter-spacing:.5px;text-align:center;color:var(--ink)}
.section-title b{font-weight:700}
.btn-outline{display:inline-block;border:1px solid var(--orange);color:var(--orange);font-size:9px;font-weight:600;padding:8px 16px;text-transform:uppercase;border-radius:2px}

/* header */
.site-header{top:0;height:87px;background:#fff}
.brand{position:absolute;left:130px;top:26px;display:flex;align-items:center;gap:10px}
.brand-dot{width:34px;height:34px;border-radius:50%;background:var(--orange)}
.brand-name{font-size:21px;font-weight:700;color:#2b4a6f}
.nav{position:absolute;top:36px;font-size:11px;color:var(--ink);text-transform:uppercase}
.nav.active{color:var(--orange)}
.search{position:absolute;left:1030px;top:25px;width:36px;height:36px;border-radius:50%;background:#aaa}
.search svg{position:absolute;left:10px;top:10px}

/* hero */
.hero{top:87px;height:533px}
.hero-photo{position:absolute;inset:0;background:linear-gradient(100deg,#cbbfb2 0%,#a59585 35%,#6b6358 60%,#3f3b36 100%)}
.hero-curve{position:absolute;left:0;bottom:0}
.hero-copy{position:absolute;left:610px;width:520px;top:155px;text-align:center;color:#fff}
.hero-title{font-family:"Oswald",Arial,sans-serif;font-weight:300;font-size:58px;letter-spacing:1px;line-height:70px;white-space:nowrap}
.hero-sub{font-size:23px;font-weight:600;line-height:37px;margin-top:10px}
.hero-btn{display:inline-block;margin-top:18px;background:var(--orange);color:#fff;font-size:11px;font-weight:600;padding:11px 14px;text-transform:uppercase}
.dots{position:absolute;left:555px;top:476px;display:flex;gap:13px}
.dots i{width:17px;height:17px;border:2px solid #fff;border-radius:50%}
.dots i:first-child{background:var(--orange)}

/* services */
.services{top:620px;height:474px}
.services .section-title{margin-top:52px}
.services .intro{width:860px;margin:14px auto 0}
.service-row{position:absolute;top:165px;left:130px;width:940px;display:flex}
.service{width:313px;text-align:center;border-right:1px solid var(--line);padding:0 30px;height:270px}
.service:last-child{border-right:0}
.service h3{font-size:11px;font-weight:700;margin-top:18px;text-transform:uppercase}
.service p{font-size:10px;line-height:18px;color:var(--muted);margin:6px 0 14px}

/* welcome */
.welcome{top:1094px;height:300px}
.welcome-panel{position:absolute;left:0;top:0;width:598px;height:300px;background:var(--orange);color:#fff;padding:48px 0 0 130px}
.welcome-panel h2{font-size:25px;font-weight:300;line-height:32px}
.welcome-panel h2 b{display:block;font-weight:700;font-size:25px}
.welcome-panel p{font-size:11px;line-height:22px;width:420px;margin-top:14px;color:#fff8ee}
.welcome-side{position:absolute;left:598px;top:0;width:602px;height:300px;background:var(--beige)}
.laptop{position:absolute;left:132px;top:40px;width:335px;height:220px;background:linear-gradient(#d9d9d9,#bdbdbd);border-radius:10px 10px 4px 4px}

/* packages */
.packages{top:1394px;height:563px;background:var(--pale)}
.packages .section-title{margin-top:44px}
.packages .intro{width:860px;margin:10px auto 0}
.plan{position:absolute;top:156px;height:285px;background:#fff;border:1px solid var(--line);text-align:center}
.plan-label{height:34px;line-height:34px;font-size:11px;text-transform:uppercase;color:#555}
.plan-price{height:80px;color:#fff;padding-top:14px}
.plan-price .amt{font-size:32px;font-weight:600;line-height:36px}
.plan-price .amt sup{font-size:13px;vertical-align:top;line-height:24px}
.plan-price .tag{font-size:10px}
.plan ul{list-style:none;font-size:11px;color:#666;line-height:28px;margin-top:16px}
.plan .btn-outline{margin-top:14px;font-size:9px;padding:6px 14px}
.plan.featured{top:140px;height:330px;box-shadow:0 2px 10px rgba(0,0,0,.12)}
.plan.featured .plan-price{height:95px}

/* testimonials */
.testimonials{top:1957px;height:330px}
.testimonials .section-title{margin-top:50px}
.quote{position:absolute;top:108px;width:296px;height:112px;border:1px solid var(--line);padding:16px 18px;box-shadow:0 1px 4px rgba(0,0,0,.05)}
.quote .mark{position:absolute;left:16px;top:10px;font-size:34px;color:#ccc;font-weight:700;line-height:30px}
.quote p{font-size:10px;font-style:italic;line-height:22px;color:var(--muted);text-indent:30px}
.quote-fold{position:absolute;right:-1px;bottom:-1px}
.author{position:absolute;top:236px;display:flex;align-items:center;gap:6px;font-size:11px}
.author small{font-size:8px;color:var(--muted)}
.author .stars{display:block;color:var(--star);font-size:10px;letter-spacing:1px;line-height:10px}
.avatar{width:30px;height:30px;background:#c9b2a6;border:2px solid #fff;box-shadow:0 0 2px rgba(0,0,0,.3)}

/* join */
.join{top:2287px;height:333px;background:linear-gradient(100deg,#6fb83c,#86c750 50%,#7dbf4a);color:#fff;text-align:center}
.join h2{font-size:35px;font-weight:700;margin-top:98px;letter-spacing:.5px}
.join p{font-size:12px;line-height:22px;width:760px;margin:10px auto 0;color:#f3fbe9}
.join-form{display:flex;justify-content:center;gap:12px;margin-top:16px}
.join-input{width:444px;height:38px;background:#fff;color:#888;font-size:11px;text-align:left;padding:11px 12px}
.join-btn{width:146px;height:38px;background:#222;color:#fff;font-size:12px;font-weight:600;line-height:38px}

/* tradies */
.tradies{top:2620px;height:363px;background:#f2f2f2}
.tradies .section-title{margin-top:42px;font-weight:700;font-size:26px}
.tradie{position:absolute;top:102px;width:160px;text-align:center}
.tradie-photo{width:160px;height:160px;background:linear-gradient(#d7d7d7,#a9a9a9)}
.tradie-name{font-size:11px;margin-top:12px}
.tradie .stars{color:var(--star);font-size:12px;letter-spacing:1px}

/* footer */
.site-footer{top:2983px;height:278px;background:var(--dark);color:#bbb}
.fcol{position:absolute;top:38px}
.fcol h4{font-size:11px;font-weight:700;color:#fff;text-transform:uppercase;letter-spacing:.5px;margin-bottom:16px}
.fcol li{list-style:none;font-size:11px;line-height:22px;color:#aaa}
.news-input{width:215px;height:36px;background:#fff;color:#999;font-size:10px;padding:11px}
.news-btn{display:inline-block;margin-top:14px;border:1px solid var(--orange);color:#fff;font-size:10px;font-weight:600;padding:8px 12px}
.contact li{display:flex;gap:8px;align-items:flex-start}
.contact li span.ic{width:11px;height:11px;background:var(--orange);margin-top:5px;flex:none;border-radius:2px}
.follow li{display:flex;align-items:center;gap:10px;margin-bottom:10px}
.follow .ring{width:34px;height:34px;border:2px solid var(--orange);border-radius:50%}
.copyright{position:absolute;left:0;top:226px;width:1200px;border-top:1px solid #3a3a3a;padding-top:16px;text-align:center;font-size:11px;color:#ccc}
</style>
</head>
<body>

<header class="site-header">
  <div class="brand"><span class="brand-dot"></span><span class="brand-name">Vetted Hammer Hub</span></div>
  <span class="nav active" style="left:482px">Home</span>
  <span class="nav" style="left:562px">About</span>
  <span class="nav" style="left:644px">Services</span>
  <span class="nav" style="left:737px">Testimonials</span>
  <span class="nav" style="left:857px">FAQ</span>
  <span class="nav" style="left:926px">Contact Us</span>
  <span class="search"><svg width="16" height="16" viewBox="0 0 16 16"><circle cx="6.5" cy="6.5" r="5" fill="none" stroke="#fff" stroke-width="2"/><line x1="10" y1="10" x2="15" y2="15" stroke="#fff" stroke-width="2"/></svg></span>
</header>

<section class="hero">
  <div class="hero-photo" role="img" aria-label="Woman using a tablet in a home-goods shop"></div>
  <svg class="hero-curve" width="1200" height="80" viewBox="0 0 1200 80"><path d="M0 40 Q600 110 1200 0 L1200 80 L0 80 Z" fill="#fff"/></svg>
  <div class="hero-copy">
    <div class="hero-title">VETTED HAMMER HUB</div>
    <div class="hero-sub">It's Now Easier Than Ever to Get Help<br>Around The House</div>
    <span class="hero-btn">Learn More Info</span>
  </div>
  <div class="dots"><i></i><i></i><i></i></div>
</section>

<section class="services">
  <h2 class="section-title">OUR <b>SERVICES</b></h2>
  <p class="lorem center intro">Lorem ipsum dolor sit amet, consectetur adipisicing elit, sed do eiusmod tempor incididunt ut labore et dolore magna aliqua. Ut enim ad minim veniam, quis nostrud exercitation ullamco laboris nisi ut aliquip proident</p>
  <div class="service-row">
    <div class="service">
      <svg width="136" height="136" viewBox="0 0 136 136"><circle cx="68" cy="68" r="64" fill="none" stroke="var(--orange-soft)" stroke-width="1.5"/><path d="M68 4 A64 64 0 1 1 9 44" fill="none" stroke="var(--blue)" stroke-width="8"/><circle cx="68" cy="68" r="50" fill="var(--blue)"/><circle cx="68" cy="58" r="8" fill="#fff"/><circle cx="50" cy="62" r="6" fill="#fff"/><circle cx="86" cy="62" r="6" fill="#fff"/><path d="M54 86 q14-22 28 0z M38 84 q12-18 20-6 M98 84 q-12-18 -20-6" fill="#fff"/></svg>
      <h3>Interview</h3>
      <p>Adipiscing elit, sed do eiusmod tempor incididunt ut labore et dolore magna aliqua...</p>
      <span class="btn-outline">Learn More</span>
    </div>
    <div class="service">
      <svg width="136" height="136" viewBox="0 0 136 136"><circle cx="68" cy="68" r="64" fill="none" stroke="var(--orange-soft)" stroke-width="1.5"/><path d="M68 4 A64 64 0 1 1 4 68" fill="none" stroke="var(--blue)" stroke-width="8"/><circle cx="68" cy="68" r="50" fill="var(--blue)"/><path d="M56 84 l4-12 20-20 8 8 -20 20z" fill="#fff"/></svg>
      <h3>Reference Check</h3>
      <p>Adipiscing elit, sed do eiusmod tempor incididunt ut labore et dolore magna aliqua...</p>
      <span class="btn-outline">Learn More</span>
    </div>
    <div class="service">
      <svg width="136" height="136" viewBox="0 0 136 136"><circle cx="68" cy="68" r="64" fill="none" stroke="var(--orange-soft)" stroke-width="1.5"/><path d="M68 4 A64 64 0 1 1 20 110" fill="none" stroke="var(--blue)" stroke-width="8"/><circle cx="68" cy="68" r="50" fill="var(--blue)"/><path d="M46 66 q22-28 44 0z" fill="#fff"/><path d="M68 66 v20 q0 6 -6 4" fill="none" stroke="#fff" stroke-width="3"/></svg>
      <h3>Verify Insurances</h3>
      <p>Adipiscing elit, sed do eiusmod tempor incididunt ut labore et dolore magna aliqua...</p>
      <span class="btn-outline">Learn More</span>
    </div>
  </div>
</section>

<section class="welcome">
  <div class="welcome-panel">
    <h2>WELCOME TO <b>VETTED HAMMER HUB</b></h2>
    <p>Lorem ipsum dolor sit amet, consectetur adipiscing elit, sed do tempo incididun ut labore et dolore magna aliqua. Ut enim ad minim veniam, quis exercitation ullamco laboris nisi ut aliquip ex ea commodo consequat...</p>
    <p>Lorem ipsum dolor sit amet, consectetur adipiscing elit, sed do tempo incididun ullamco laboris nisi ut aliquip ex ea commodo consequat...</p>
  </div>
  <div class="welcome-side">
    <div class="laptop" role="img" aria-label="Laptop showing the Vetted Hammer Hub home screen"></div>
  </div>
</section>

<section class="packages">
  <h2 class="section-title">PRODUCTS <b>PACKAGES</b></h2>
  <p class="lorem center intro">Lorem ipsum dolor sit amet, consectetur adipiscing elit, sed do eiusmod tempor incididunt ut labore et dolore magna veniam, quis nostrud exercitation ullamco laboris nisi ut aliquip proident</p>

  <div class="plan" style="left:130px;width:218px">
    <div class="plan-label" style="background:#e6f1f3">Product Name</div>
    <div class="plan-price" style="background:var(--teal)"><div class="amt"><sup>$</sup>9</div><div class="tag">Limited Time Offer</div></div>
    <ul><li>Excepteur sint occaecat</li><li>Cupidatat Proiden</li><li>Exercitation ullamco</li><li>Nemo enim</li></ul>
    <span class="btn-outline" style="border-color:var(--teal);color:var(--teal)">Sign Up Now</span>
  </div>

  <div class="plan featured" style="left:350px;width:260px">
    <div class="plan-label" style="background:#f4efe7">Product Name</div>
    <div class="plan-price" style="background:var(--orange);padding-top:20px"><div class="amt"><sup>$</sup>46</div><div class="tag">Limited Time Offer</div></div>
    <ul><li>Excepteur sint occaecat</li><li>Cupidatat Proiden</li><li>Exercitation ullamco</li><li>Nemo enim</li></ul>
    <span class="btn-outline">Sign Up Now</span>
  </div>

  <div class="plan" style="left:612px;width:214px">
    <div class="plan-label" style="background:#f8e6e6">Product Name</div>
    <div class="plan-price" style="background:var(--red)"><div class="amt"><sup>$</sup>17</div><div class="tag">Limited Time Offer</div></div>
    <ul><li>Excepteur sint occaecat</li><li>Cupidatat Proiden</li><li>Exercitation ullamco</li><li>Nemo enim</li></ul>
    <span class="btn-outline" style="border-color:var(--red);color:var(--red)">Sign Up Now</span>
  </div>

  <div class="plan" style="left:840px;width:228px">
    <div class="plan-label" style="background:#f5f0df">Product Name</div>
    <div class="plan-price" style="background:var(--yellow)"><div class="amt"><sup>$</sup>22</div><div class="tag">Limited Time Offer</div></div>
    <ul><li>Excepteur sint occaecat</li><li>Cupidatat Proiden</li><li>Exercitation ullamco</li><li>Nemo enim</li></ul>
    <span class="btn-outline" style="border-color:var(--yellow);color:var(--yellow)">Sign Up Now</span>
  </div>
</section>

<section class="testimonials">
  <h2 class="section-title">WHAT OUR <b>CUSTOMER SAY'S</b></h2>

  <div class="quote" style="left:132px"><span class="mark">&ldquo;</span><p>Mauris quis sodales enim, semper ultric les massa. Pellentesque risus dolor, tristique vel facilisis at, laoreet ut elit. Fusce id augue...</p><svg class="quote-fold" width="30" height="20"><path d="M30 0 L30 20 L0 20 Z" fill="#ddd"/></svg></div>
  <div class="author" style="left:226px"><div>Liam Porter, <small>City name</small><span class="stars">★★★★★</span></div><div class="avatar" role="img" aria-label="Customer portrait"></div></div>

  <div class="quote" style="left:452px"><span class="mark">&ldquo;</span><p>Mauris quis sodales enim, semper ultric les massa. Pellentesque risus dolor, tristique vel facilisis at, laoreet ut elit. Fusce id augue...</p><svg class="quote-fold" width="30" height="20"><path d="M30 0 L30 20 L0 20 Z" fill="#ddd"/></svg></div>
  <div class="author" style="left:545px"><div>Liam Porter, <small>City name</small><span class="stars">★★★★★</span></div><div class="avatar" role="img" aria-label="Customer portrait"></div></div>

  <div class="quote" style="left:770px"><span class="mark">&ldquo;</span><p>Mauris quis sodales enim, semper ultric les massa. Pellentesque risus dolor, tristique vel facilisis at, laoreet ut elit. Fusce id augue...</p><svg class="quote-fold" width="30" height="20"><path d="M30 0 L30 20 L0 20 Z" fill="#ddd"/></svg></div>
  <div class="author" style="left:865px"><div>Liam Porter, <small>City name</small><span class="stars">★★★★★</span></div><div class="avatar" role="img" aria-label="Customer portrait"></div></div>
</section>

<section class="join" role="img" aria-label="Green-tinted photo of tradespeople at work behind the sign-up band">
  <h2>TRADESPEOPLE TO JOIN</h2>
  <p>We are an experienced consulting company and recruit successful professionals and executives for companies. We place particular emphasis on the needs of our candidates and clients, who benefit from</p>
  <div class="join-form"><div class="join-input">email</div><div class="join-btn">JOIN NOW!</div></div>
</section>

<section class="tradies">
  <h2 class="section-title">TRADIES</h2>
  <div class="tradie" style="left:132px"><div class="tradie-photo" role="img" aria-label="Tradesperson portrait"></div><div class="tradie-name">Liam Porter</div><div class="stars">★★★★★</div></div>
  <div class="tradie" style="left:326px"><div class="tradie-photo" role="img" aria-label="Tradesperson portrait"></div><div class="tradie-name">Liam Porter</div><div class="stars">★★★★★</div></div>
  <div class="tradie" style="left:520px"><div class="tradie-photo" role="img" aria-label="Tradesperson portrait"></div><div class="tradie-name">Liam Porter</div><div class="stars">★★★★★</div></div>
  <div class="tradie" style="left:715px"><div class="tradie-photo" role="img" aria-label="Tradesperson portrait"></div><div class="tradie-name">Liam Porter</div><div class="stars">★★★★★</div></div>
  <div class="tradie" style="left:908px"><div class="tradie-photo" role="img" aria-label="Tradesperson portrait"></div><div class="tradie-name">Liam Porter</div><div class="stars">★★★★★</div></div>
</section>

<footer class="site-footer">
  <div class="fcol" style="left:133px"><h4>Quick Links</h4><ul><li>Home</li><li>About Us</li><li>Services</li><li>Testimonials</li><li>FAQ's</li><li>Contact Us</li></ul></div>
  <div class="fcol" style="left:274px"><h4>Information</h4><ul><li>Terms &amp; Conditions</li><li>Privacy Policy</li><li>Disclaimer</li><li>Site Map</li></ul></div>
  <div class="fcol" style="left:449px"><h4>Newsletter</h4><div class="news-input">Enter Email Address</div><span class="news-btn">SUBSCRIBE</span></div>
  <div class="fcol contact" style="left:730px;width:190px"><h4>Contact Details</h4><ul><li><span class="ic"></span>(555) 210-3870</li><li><span class="ic"></span>(555) 210-3870</li><li><span class="ic"></span>hello@vettedhammerhub.example</li><li><span class="ic"></span>82868 Lorem ipsum dolor sit amet, consectetur</li></ul></div>
  <div class="fcol follow" style="left:965px"><h4>Follow Us</h4><ul><li><span class="ring"></span>Community</li><li><span class="ring"></span>Updates</li><li><span class="ring"></span>Circles</li></ul></div>
  <div class="copyright">Copyrights © Vetted Hammer Hub , 2017 | All rights reserved.</div>
</footer>

</body>
</html>
```